Neues Corporate Design für Steuerberaterin
Zielgruppe
Ich bin seit Kurzem als Steuerberaterin selbständig tätig. Meine Zielgruppe sind v.a. junge engagierte Leute zwischen 25 und 45 Jahren - Privatpersonen als auch Unternehmer - die ein bisschen anders denken und sich beim herkömmlichen Steuerberater nicht gut aufgehoben fühlen. Mir ist auch der persönliche/menschliche Aspekt mit meinen Kunden sehr wichtig (im Gegensatz zu vielen anderen), denn fachlich top sind eh die meisten und mein Eindruck ist, das alleine reicht nicht mehr aus.
Aufgabenstellung
Ich habe mich in den vergangenen Jahren bereits ein bisschen auf die Selbständigkeit vorbereitet und u.a. auch eine Visitenkarte entworfen (siehe Anhang). Allerdings ist das schon etwas länger her und ich finde diese 'alte' Visitenkarte nicht mehr ganz zeitgemäß bzw. auch zu undurchdacht. Das Logo (Weintraube und Paragraph) finde ich auch nicht mehr so passend (und etwas unseriös). Mir wär lieber ein schönen Schriftzug oder ein Logo mit Initialen oder sonst etwas Kreatives, damit das Ganze etwas professioneller wirkt. Meine Lieblingsfarbe ist violett, es kann aber auch gerne hell und dunkel gemischt werden. Ich könnte mir ebenfalls ein Farbspiel mit Kreisen oder Ecken oder sonst etwas vorstellen. Auf der Vorderseite der Visitenkarte hätte ich gerne 'Lena Brunner - Steuerberatung' stehen. Auf der Rückseite dann 'Steuerberaterin MMag. Lena Brunner' und alle Informationen die auch im Anhang zu finden sind. Ganz unten sollen graphisch abgegrenzt beiden Büro-Adressen stehen. So zumindest mal mein Vorschlag, bin aber auch für andere Ideen offen.

```html
<!DOCTYPE html>
<html lang="de">
<head>
<meta charset="utf-8">
<title>Lena Brunner – Steuerberatung Visitenkarte</title>
<link rel="stylesheet" href="https://fonts.googleapis.com/css2?family=Cinzel:wght@600&family=Oswald:wght@300&family=Open+Sans:ital,wght@1,300&family=Jost:wght@400;600&display=swap">
<style>
  :root {
    --plum: #4a0f4f;
    --paper: #ffffff;
    --canvas: #ffffff;
    --muted: #555555;
    --edge: #dcdcdc;
  }
  * { margin: 0; padding: 0; box-sizing: border-box; }
  html, body { width: 1200px; height: 1200px; overflow: hidden; background: var(--canvas); }
  .canvas { position: relative; width: 1200px; height: 1200px; }

  .card { position: absolute; left: 275px; width: 650px; height: 380px; }
  .card-front { top: 140px; background: var(--plum); color: var(--paper); }
  .card-back { top: 585px; background: var(--paper); border: 1px solid var(--edge); }

  /* Front */
  .front-mark {
    position: absolute; left: 50%; top: 95px; transform: translateX(-50%);
    width: 92px; height: 92px; border: 2px solid var(--paper);
  }
  .front-name {
    position: absolute; left: 0; right: 0; top: 205px; text-align: center;
    font-family: "Cinzel", serif; font-weight: 600; font-size: 34px; letter-spacing: 0.5px;
  }
  .front-tagline {
    position: absolute; left: 0; right: 0; top: 252px; text-align: center;
    font-family: "Oswald", sans-serif; font-weight: 300; font-size: 15px;
    letter-spacing: 13px; padding-left: 13px; text-transform: uppercase;
  }

  /* Back */
  .back-name {
    position: absolute; left: 30px; top: 60px; color: var(--plum);
    font-family: "Cinzel", serif; font-weight: 600; font-size: 37px; letter-spacing: 0.3px;
  }
  .back-title {
    position: absolute; left: 30px; top: 107px; color: var(--muted);
    font-family: "Open Sans", sans-serif; font-style: italic; font-weight: 300; font-size: 19px;
    text-transform: uppercase; letter-spacing: -0.3px;
  }
  .back-mark {
    position: absolute; left: 437px; top: 60px; width: 162px; height: 162px;
    border: 2px solid var(--plum); display: flex; align-items: center; justify-content: center;
    text-align: center; color: var(--plum);
    font-family: "Cinzel", serif; font-weight: 600; font-size: 24px; line-height: 1.25;
  }
  .contact-band {
    position: absolute; left: 0; right: 0; bottom: 0; height: 103px; background: var(--plum);
    color: var(--paper); font-family: "Jost", sans-serif; font-weight: 400; font-size: 19px;
    display: grid; grid-template-columns: 297px 1fr; padding: 21px 0 0 29px; row-gap: 6px;
    align-content: start;
  }
  .contact-band .label { font-weight: 600; }
</style>
</head>
<body>
<main class="canvas">
  <section class="card card-front" aria-label="Vorderseite">
    <div class="front-mark"></div>
    <div class="front-name">LENA BRUNNER</div>
    <div class="front-tagline">Steuerberatung</div>
  </section>

  <section class="card card-back" aria-label="Rückseite">
    <h1 class="back-name">LENA BRUNNER</h1>
    <p class="back-title">Steuerberaterin MMag.</p>
    <div class="back-mark">Lena<br>Brunner</div>
    <div class="contact-band">
      <span>Strasse 123 12345 Stadt</span>
      <span><span class="label">Email</span> info@lenabrunner.de</span>
      <span><span class="label">Tel</span> 12 / 123 456 78</span>
      <span><span class="label">Web</span> www.lenabrunner.de</span>
    </div>
  </section>
</main>
</body>
</html>
```